Business Card Design

We need a business card design that can also be aplied for postcards. We are a small indie record company that also do consulting, and development of independat artitst . I already have the name and the basic idea of what i am looking for but i am open to any suggestion.
Info for the card
Name of the company : Velmora Records
NAME : Tomas Invaldi
PHONE : 208-5536142
EMAIL : hello@velmorarecords.example
WEB: www.velmorarecords.example
Target Market(s)
Male - Female independent musicians ages 18 to 45
Industry/Entity Type
Record Company
Contact Information for Business Card
Independant records company that also works in consulting for music business models for independent artists
Look and feel
Each slider illustrates characteristics of the customer's brand and the style your logo design should communicate.

```html
<!DOCTYPE html>
<html lang="en">
<head>
<meta charset="utf-8">
<title>Velmora Records — Business Card</title>
<link rel="stylesheet" href="https://fonts.googleapis.com/css2?family=Roboto+Condensed:wght@700&family=Arimo:wght@700&display=swap">
<style>
  :root {
    --sky: #5a9cc0;
    --navy: #02547f;
    --white: #ffffff;
  }
  html, body {
    margin: 0;
    padding: 0;
    overflow: hidden;
    background: var(--white);
  }
  .card {
    position: relative;
    width: 1200px;
    height: 704px;
    overflow: hidden;
    background: var(--navy);
    font-family: "Arimo", Arial, sans-serif;
    color: var(--white);
  }
  .card__header {
    position: absolute;
    left: 0; top: 0;
    width: 1200px;
    height: 405px;
    background: var(--sky);
  }
  .brand-name {
    position: absolute;
    left: 0; top: 160px;
    width: 1200px;
    margin: 0;
    text-align: center;
    font-family: "Arimo", Arial, sans-serif;
    font-weight: 700;
    font-size: 76px;
    line-height: 1;
    word-spacing: 0.08em;
    color: var(--white);
  }
  .person-name {
    position: absolute;
    left: 77px; top: 498px;
    margin: 0;
    font-family: "Roboto Condensed", "Arial Narrow", sans-serif;
    font-weight: 700;
    font-size: 60px;
    line-height: 1;
  }
  .contact {
    position: absolute;
    left: 668px; top: 480px;
    width: 497px;
    height: 160px;
    text-align: center;
    font-style: normal;
    font-size: 25px;
    font-weight: 700;
  }
  .contact__item {
    position: absolute;
    left: 0; width: 100%;
    margin: 0;
    line-height: 1;
  }
  .contact__email { top: 6px; }
  .contact__divider {
    position: absolute;
    left: 0; top: 48px;
    width: 100%;
    height: 3px;
    background: var(--white);
  }
  .contact__web { top: 62px; }
  .contact__phone { top: 121px; }
  .footer-stripes {
    position: absolute;
    left: 0; top: 648px;
  }
</style>
</head>
<body>
  <main class="card">
    <header class="card__header">
      <h1 class="brand-name">Velmora Records</h1>
    </header>

    <p class="person-name">Tomas Invaldi</p>

    <address class="contact">
      <p class="contact__item contact__email">hello@velmorarecords.example</p>
      <span class="contact__divider"></span>
      <p class="contact__item contact__web">www.velmorarecords.example</p>
      <p class="contact__item contact__phone">208-5536142</p>
    </address>

    <svg class="footer-stripes" width="1200" height="22" viewBox="0 0 1200 22" aria-hidden="true">
      <rect x="0" y="0" width="1200" height="21" fill="var(--sky)"/>
      <polygon points="493,21 524,2 1200,2 1200,21" fill="var(--white)"/>
    </svg>
  </main>
</body>
</html>
```